One of Australia's fastest growing energy maintenance contractors needs a new website

www.panelbrite.com.au
Our business has evolved over the past years and now our website is no longer relevant.
We clean solar panels and we vacuum roof gutters.
We clean solar panels on the roofs of residential houses right up to billion dollar solar farms with in excess of 1 million panels. We offer thermal image testing and bird proofing for our residential and commercial clients and thermal drone imaging services for our solar farm clients.
We vacuum clean roof gutters (using a LoftSuk) on the residential house next door right up to enormous private and public schools, colleges, shopping centres, strat complexes and commercial buildings.
When first built our business had more of a domestic residential skew and the website reflected that. While that is still part of our core business we are now bidding on and have secured large government, commercial and infrastructure contracts and our new website needs to reflect our growth and our new business. We need a new site that it optimised for both desktop ad phone viewing as our latest figures showed that 73% of people visiting our site are on mobile phones. We have an extensive amount of data on Trekmetrics available as well as Bidlinks. Both that would also need integrating with the site along with a few other plugins such as Kembo Chat IQ, Friendwall etc along with SEO key words etc. We are also the winner and finalists over multiple years of the small business of the year awards and we like to proudly and prominently display those on our site.
We are looking for a new site with a modern professional feel / theme
There is a definitive break in our business between the solar Panel cleaning clients and the gutter cleaning clients so we would like a home page that begins with a simple choice:
Solar Panel Cleaning – Gutter Cleaning
With a professional full screen background image (we have hundreds to choose from) and along the bottom a small area with rights reserved etc, phone number etc (at some point in the future we will split these into two businesses but for now it’s what we have).
After that selection is made we would like a repeat of that same scenario but the selection is:
If it’s Solar Panel Cleaning
(new background image)
Government – Infrastructure – Commercial – Residential
If it’s Gutter Cleaning
(new background image)
Government – Strata – Commercial – Residential
After making those choices then onto the relevant pages with background images relevant to each sector and a them that suits (on the residential we would like to keep the link to our trekmetrics reviews) - We will provide copy / text for each relevant page.
Other than that, a menu inclusive of the above and:
Resellers Portal – we will provide a link to this from Kembo CRM)
Customer portal (we will supply a link to this from our booking system)
We also need a page for our Solar Resellers / Partners page but we will give them a link to this, it won’t be listed on the site.
Request a quote page (Again we will provide information from Kembo as this will be linked to the CRM)
Standard contact us page inclusive of phone numbers, address and fields supplied from CRM
Sydney – 02 7391 5084
Southern Highlands – 02 4863 1507
Goulburn – 02 4863 1507
Canberra – 02 6178 3045
Wollongong – 02 4239 7615
sales@panelbrite.com.au
Head Office - Ferndell NSW 2583
ABN: 48762093115
Responsive Design: Optimized for desktop and mobile (73% mobile visitors).
Fast Loading Speed: Optimized for performance.
Smooth Transition Animations: For service and category selection.
Sticky Contact Bar: Always accessible at the bottom of mobile screens for quick calls.
SEO Optimization: Focused on government tenders, large-scale commercial contracts, and infrastructure projects.
Integrations
Trekmetrics & Trekmetrics Bidlinks.
Kembo Chat IQ.
Friendwall Beacon.
SEO tools and keyword optimization.
Many many more images available if needed

```html
<!DOCTYPE html>
<html lang="en">
<head>
<meta charset="utf-8">
<title>PanelBrite – Commercial Solar Panel Cleaning</title>
<link href="https://fonts.googleapis.com/css2?family=Manrope:wght@300;400;500;600&display=swap" rel="stylesheet">
<style>
:root{
  --blue:#0f7fd6;
  --blue-dark:#0a63b8;
  --navy:#00264a;
  --ink:#1b2330;
  --muted:#3e4956;
  --card:#f4f4f4;
  --review:#8fa1b4;
  --white:#ffffff;
  --star:#f5b90f;
}
*{box-sizing:border-box;margin:0;padding:0}
html,body{width:1200px;height:2642px;overflow:hidden}
body{font-family:"Manrope",sans-serif;color:var(--ink);background:var(--white);position:relative}
.abs{position:absolute}
.btn{position:absolute;display:flex;align-items:center;justify-content:center;background:linear-gradient(180deg,#1a90e6,var(--blue-dark));color:var(--white);font-size:14px;font-weight:500;border-radius:6px}

/* hero */
.hero{position:absolute;left:0;top:0;width:1200px;height:853px;overflow:hidden}
.hero-photo{position:absolute;inset:0;background:linear-gradient(160deg,#3d5640 0%,#4b5a66 25%,#2c3b5c 50%,#6a3d35 75%,#4a3a3a 100%)}
.hero-shade{position:absolute;inset:0;background:rgba(10,18,30,.35)}
.logo{position:absolute;display:flex;align-items:center;gap:10px;font-weight:500;font-size:26px}
.logo-dot{width:34px;height:34px;border-radius:50%}
.hero .logo{left:100px;top:18px;color:#1d8fe2}
.hero .logo-dot{background:#1d8fe2}
.nav{position:absolute;top:28px;right:280px;display:flex;gap:20px;color:var(--white);font-size:14px}
.hero h1{position:absolute;left:0;width:1200px;top:266px;text-align:center;color:var(--white);font-weight:300;font-size:56px;line-height:64px}
.hero .lead{position:absolute;top:413px;width:1200px;text-align:center;color:var(--white);font-size:14px}
.hero .body{position:absolute;top:466px;left:260px;width:680px;text-align:center;color:var(--white);font-size:14px;line-height:20px;font-weight:300}
.features{position:absolute;top:742px;left:100px;display:flex}
.feature{width:255px;display:flex;gap:8px;align-items:center;color:var(--white);font-size:14px;line-height:20px;font-weight:300}
.feature svg{flex:none}

/* sectors */
.sectors h2{position:absolute;left:100px;top:998px;font-size:42px;font-weight:400;line-height:48px;width:420px}
.sectors p{position:absolute;left:100px;top:1156px;width:400px;font-size:14px;line-height:20px;color:var(--muted)}
.sector{position:absolute;width:235px;height:167px;background:var(--card);border-radius:12px;padding:20px 13px}
.sector span{position:absolute;left:13px;bottom:20px;font-size:18px;line-height:21px}

/* reviews */
.reviews{position:absolute;left:0;top:1340px;width:1200px;height:612px;background:var(--navy);overflow:hidden;color:var(--white)}
.reviews h2{position:absolute;left:100px;top:69px;font-size:42px;font-weight:400}
.reviews .intro{position:absolute;left:100px;top:130px;width:720px;font-size:14px;line-height:20px;font-weight:300}
.review{position:absolute;top:202px;width:490px;height:266px;background:var(--review);border-radius:12px;padding:20px;color:#f3f6f9}
.avatar{position:absolute;left:20px;top:20px;width:46px;height:46px;border-radius:50%;background:#4a5560}
.who{position:absolute;left:76px;top:24px;font-size:13px;font-weight:500;color:#162230}
.when{position:absolute;left:76px;top:48px;font-size:12px;color:#3b4756}
.stars{position:absolute;right:20px;top:32px;display:flex;gap:6px}
.review .text{position:absolute;left:20px;top:96px;width:450px;font-size:13.5px;line-height:20px;color:#2c3846}
.arrow{position:absolute;top:502px;width:43px;height:43px;border-radius:50%;display:flex;align-items:center;justify-content:center}

/* call to action */
.cta-photo{position:absolute;left:100px;top:2018px;width:562px;height:294px;border-radius:20px;background:linear-gradient(180deg,#5b7a54 0%,#8ea08a 45%,#a9b0ba 75%,#c8ccd3 100%)}
.cta h2{position:absolute;left:695px;top:2054px;font-size:42px;font-weight:400;line-height:48px}
.cta p{position:absolute;left:695px;top:2162px;width:400px;font-size:14px;line-height:20px;color:var(--muted)}

/* footer */
.footer{position:absolute;left:0;top:2378px;width:1200px;height:264px;background:linear-gradient(180deg,#1ba0e0 0%,#0c6bc4 100%);color:var(--white)}
.footer .logo{left:100px;top:38px;color:var(--white)}
.footer .logo-dot{background:var(--white)}
.abn{position:absolute;left:100px;top:87px;font-size:14px}
.f-label{font-size:14px;font-weight:500}
.f-value{font-size:14px;font-weight:300;margin-top:6px;color:#e3f1fb}
.rule{position:absolute;left:100px;top:120px;width:1000px;height:1px;background:rgba(255,255,255,.3)}
.cities{position:absolute;left:100px;top:139px;display:flex}
.city{width:204px}
.copy{position:absolute;top:217px;width:1200px;text-align:center;font-size:13px}
</style>
</head>
<body>

<header class="hero">
  <div class="hero-photo" role="img" aria-label="Technician in hi-vis workwear cleaning rows of solar panels on a red commercial roof"></div>
  <div class="hero-shade"></div>
  <div class="logo"><span class="logo-dot"></span>PanelBrite</div>
  <nav class="nav"><span>Resellers</span><span>Customers</span></nav>
  <div class="btn" style="left:942px;top:15px;width:158px;height:43px">Request A Quote</div>
  <h1>Maximize Solar Efficiency for Your<br>Business</h1>
  <div class="lead">Ensuring peak energy output with professional commercial solar panel cleaning.</div>
  <div class="body">Solar panels are a significant investment for businesses, contributing to lower energy costs and sustainability goals. However, dirt, dust, and debris can reduce efficiency by up to 30%. Our expert cleaning services ensure your panels perform at their best, maximizing ROI and longevity.</div>
  <div class="btn" style="left:538px;top:546px;width:124px;height:43px">Contact Us</div>
  <div class="features">
    <div class="feature"><svg width="42" height="42" viewBox="0 0 42 42" fill="none" stroke="#fff" stroke-width="1.8"><circle cx="21" cy="21" r="7"/><path d="M21 3v6M21 33v6M3 21h6M33 21h6M8 8l4 4M30 30l4 4M8 34l4-4M30 12l4-4"/><circle cx="21" cy="21" r="13"/></svg>Industry-grade cleaning techniques</div>
    <div class="feature"><svg width="42" height="42" viewBox="0 0 42 42" fill="none" stroke="#fff" stroke-width="1.8"><path d="M4 6c20 0 34 8 34 24-14 4-28-2-30-14M4 6l30 32"/></svg>Non-abrasive, eco-friendly solutions</div>
    <div class="feature"><svg width="42" height="42" viewBox="0 0 42 42" fill="none" stroke="#fff" stroke-width="1.8"><path d="M21 3l16 6v12c0 10-8 16-16 18C13 37 5 31 5 21V9z"/><path d="M14 21l5 5 9-10"/></svg>Certified professionals with years of experience</div>
    <div class="feature"><svg width="42" height="42" viewBox="0 0 42 42" fill="none" stroke="#fff" stroke-width="1.8"><rect x="3" y="7" width="36" height="32" rx="3"/><path d="M3 15h36M12 3v8M30 3v8"/><g fill="#fff" stroke="none"><circle cx="11" cy="22" r="2"/><circle cx="18" cy="22" r="2"/><circle cx="25" cy="22" r="2"/><circle cx="32" cy="22" r="2"/><circle cx="11" cy="31" r="2"/><circle cx="18" cy="31" r="2"/><circle cx="25" cy="31" r="2"/></g></svg>Scheduled maintenance plans for long-term efficiency</div>
  </div>
</header>

<section class="sectors">
  <h2>Tailored Cleaning for Every Commercial Space</h2>
  <p>From offices to industrial sites, our expert cleaning solutions ensure maximum solar efficiency for businesses of all sizes.</p>
  <div class="sector" style="left:610px;top:920px"><svg width="32" height="32" viewBox="0 0 32 32" fill="none" stroke="#0f7fd6" stroke-width="1.6"><rect x="2" y="8" width="28" height="20" rx="3"/><path d="M11 8V5h10v3M2 16h28M14 16v3h4v-3"/></svg><span>Offices &amp; Corporate Buildings</span></div>
  <div class="sector" style="left:865px;top:920px"><svg width="32" height="32" viewBox="0 0 32 32" fill="none" stroke="#0f7fd6" stroke-width="1.6"><path d="M2 4h5l4 16h16l3-11H9"/><circle cx="13" cy="26" r="2"/><circle cx="25" cy="26" r="2"/></svg><span>Shopping Centers &amp; Retail Stores</span></div>
  <div class="sector" style="left:610px;top:1107px"><svg width="32" height="32" viewBox="0 0 32 32" fill="none" stroke="#0f7fd6" stroke-width="1.6"><path d="M3 29l15-15M14 10l6-6c4 0 8 3 9 7l-4-1-5 5z"/></svg><span>Industrial &amp; Manufacturing Facilities</span></div>
  <div class="sector" style="left:865px;top:1107px"><svg width="32" height="32" viewBox="0 0 32 32" fill="none" stroke="#0f7fd6" stroke-width="1.6"><path d="M3 26V15h26v11M3 21h26M6 15V7h20v8M9 15v-4h6v4M17 15v-4h6v4"/></svg><span>Hotels &amp; Hospitality Venues</span></div>
</section>

<section class="reviews">
  <h2>What Our Clients Say</h2>
  <p class="intro">Trusted by businesses and homeowners alike, our expert cleaning services deliver real results. See what our satisfied clients have to say!</p>
  <div class="btn" style="left:954px;top:125px;width:146px;height:43px">Write A Review</div>

  <article class="review" style="left:-142px">
    <div class="when" style="left:142px">25</div>
    <div class="stars"><svg width="120" height="20" viewBox="0 0 120 20" fill="var(--star)"><path id="st" d="M10 1l2.6 6 6.4.5-4.9 4.2 1.5 6.3L10 14.7 4.4 18l1.5-6.3L1 7.5 7.4 7z"/><use href="#st" x="26"/><use href="#st" x="52"/><use href="#st" x="78"/><use href="#st" x="104"/></svg></div>
    <div class="text" style="left:142px;width:330px">round.<br>ob and get a quote.<br>as reasonable.<br>ne to do the work was on time (to the minute!) polite<br>roughout.<br>otos showed what a good job they did.<br>d panelbrite.com.au to anyone.</div>
  </article>

  <article class="review" style="left:355px">
    <div class="avatar"></div>
    <div class="who">Corwin Albury</div>
    <div class="when">12 December 2024</div>
    <div class="stars"><svg width="124" height="20" viewBox="0 0 124 20" fill="var(--star)"><use href="#st"/><use href="#st" x="26"/><use href="#st" x="52"/><use href="#st" x="78"/><use href="#st" x="104"/></svg></div>
    <div class="text">Another excellent service from PanelBrite. Arrived on time and completed the job well. Easy to deal with and great technician. We will have them again.</div>
  </article>

  <article class="review" style="left:852px">
    <div class="avatar"></div>
    <div class="who">Tam R</div>
    <div class="when">5 December 2024</div>
    <div class="text" style="width:360px">Amazing job cleaning out my gutters. It was sunny and a lot more dirt in the gutters than i expected and a bit complaints from the cleaner. Great work. Would recom and family.</div>
  </article>

  <div class="arrow" style="left:547px;border:1px solid #fff"><svg width="12" height="12" viewBox="0 0 12 12" fill="none" stroke="#fff" stroke-width="1.6"><path d="M8 1L3 6l5 5"/></svg></div>
  <div class="arrow" style="left:610px;background:var(--blue)"><svg width="12" height="12" viewBox="0 0 12 12" fill="none" stroke="#fff" stroke-width="1.6"><path d="M4 1l5 5-5 5"/></svg></div>
</section>

<section class="cta">
  <div class="cta-photo" role="img" aria-label="Crew in orange safety gear washing a large rooftop solar array with extension brushes"></div>
  <h2>Boost Your Solar Efficiency Today!</h2>
  <p>Don't let dirt and debris reduce your energy savings. Get expert cleaning tailored to your business needs</p>
  <div class="btn" style="left:695px;top:2235px;width:124px;height:43px">Contact Us</div>
</section>

<footer class="footer">
  <div class="logo"><span class="logo-dot"></span>PanelBrite</div>
  <div class="abn">ABN: 48762093115</div>
  <div class="abs" style="left:798px;top:53px"><div class="f-label">Mail</div><div class="f-value">sales@panelbrite.com.au</div></div>
  <div class="abs" style="left:974px;top:53px"><div class="f-label">Head Office</div><div class="f-value">Ferndell NSW 2583</div></div>
  <div class="rule"></div>
  <div class="cities">
    <div class="city"><div class="f-label">Sydney</div><div class="f-value">02 7391 5084</div></div>
    <div class="city"><div class="f-label">Southern Highlands</div><div class="f-value">02 4863 1507</div></div>
    <div class="city"><div class="f-label">Goulburn</div><div class="f-value">02 4863 1507</div></div>
    <div class="city"><div class="f-label">Canberra</div><div class="f-value">02 6178 3045</div></div>
    <div class="city"><div class="f-label">Wollongong</div><div class="f-value">02 4239 7615</div></div>
  </div>
  <div class="copy">© PanelBrite 2025, All Rights Reserved.</div>
</footer>

</body>
</html>
```